ReelVows Identity
Pamphlet/Business Cards
@PH - please check your private message on top right once you login to your pixelhive account & reply.
Thanks
Hi, I like the card on top, but please don't include my contact info...
It should include things like "Toronto, Montreal, Ottawa, Vancouver, Calgary, Edmonton", website reelvows-example.ca, phone 1.877.555.0148, email info@reelvows-example.ca and facebook reelvows-example.ca/social
We need a business card and 4x6 pamphlet designs, styled similar to our website http://reelvows-example.ca

```html
<!DOCTYPE html>
<html lang="en">
<head>
<meta charset="utf-8">
<title>ReelVows Identity – Pamphlet and Business Cards</title>
<link href="https://fonts.googleapis.com/css2?family=Cinzel:wght@400;700&family=Open+Sans:wght@400;600;700&display=swap" rel="stylesheet">
<style>
:root{
  --bg:#e9e4dd;
  --ink:#0b0b0b;
  --glow:#3a3a3a;
  --white:#f4f4f4;
  --muted:#b5b5b5;
  --dim:#7a7a7a;
  --orange:#e8862a;
  --blue:#5aa6dc;
  --line:#5a5a5a;
}
*{margin:0;padding:0;box-sizing:border-box}
html,body{width:1200px;height:631px;overflow:hidden}
body{background:var(--bg);position:relative;font-family:"Open Sans",Arial,sans-serif;color:var(--white)}
.sheet{position:absolute;background:radial-gradient(ellipse at 50% 35%,var(--glow) 0%,var(--ink) 70%);box-shadow:0 2px 8px rgba(0,0,0,.25);overflow:hidden}
.flyer-front{left:132px;top:36px;width:408px;height:576px}
.flyer-back{left:560px;top:36px;width:388px;height:576px}
.brand{position:absolute;text-align:center}
.brand-dot{width:46px;height:46px;border-radius:50%;border:1px solid var(--muted);margin:0 auto 4px}
.brand-name{font-family:"Cinzel",Georgia,serif;font-weight:700;font-size:15px;letter-spacing:1px;color:var(--white)}
.sparkle{position:absolute;left:18px;top:18px;width:74px;height:74px;border-radius:50%;background:radial-gradient(circle,#cfcfcf 0%,#555 45%,transparent 72%)}
.headline{position:absolute;left:0;right:0;text-align:center;font-weight:700;font-size:22px;line-height:1.18;color:var(--white)}
.headline .accent{color:var(--orange)}
.photo{position:absolute;left:44px;top:178px;width:320px;height:262px;border:3px solid #d8d8d8;background:linear-gradient(160deg,#d9cbb4 0%,#8c7a60 55%,#3d3327 100%)}
.serves{position:absolute;top:452px;left:0;right:0;text-align:center}
.serves h3{color:var(--orange);font-size:13px;font-weight:600}
.serves p{font-size:10px;color:var(--muted);margin-top:2px}
.contact-row{position:absolute;top:496px;left:24px;right:24px;display:flex;justify-content:space-between;font-size:9px;color:var(--muted);line-height:1.5}
.contact-row .right{text-align:right}
.footer-bar{position:absolute;left:0;right:0;bottom:0;height:30px;background:#050505;border-top:1px solid var(--line);display:flex;justify-content:space-between;align-items:center;padding:0 20px;font-size:10px;color:var(--white)}
.footer-bar b{color:var(--orange);font-size:12px}
.city-menu{position:absolute;right:10px;top:10px;width:70px;background:#1e1e1e;border:1px solid var(--line);padding:4px 6px;font-size:7.5px;line-height:1.45;color:var(--muted)}
.city-menu li{list-style:none}
.packages{position:absolute;left:26px;right:22px;top:176px;font-size:8px;line-height:1.45;color:var(--muted)}
.packages h4{color:var(--white);font-size:10px;font-weight:700;margin-top:8px}
.packages .lead{color:var(--dim)}
.packages ul{padding-left:10px}
.offer{position:absolute;left:0;right:0;top:472px;text-align:center;color:var(--blue);font-size:15px;line-height:1.2;font-weight:600}
.card{position:absolute;left:972px;width:216px;height:132px;background:linear-gradient(180deg,#1b1b1b,#060606);box-shadow:0 2px 6px rgba(0,0,0,.25);overflow:hidden}
.card-front{top:180px}
.card-back{top:336px}
.card-cities{position:absolute;top:8px;right:10px;font-size:7px;color:var(--orange)}
.card-brand{left:14px;top:34px}
.card-brand .brand-dot{width:32px;height:32px}
.card-brand .brand-name{font-size:10px}
.card-contact{position:absolute;left:98px;top:48px;font-size:6.5px;color:var(--muted);line-height:1.7}
.card-mark{position:absolute;left:0;right:0;top:38px;text-align:center;font-family:"Cinzel",Georgia,serif;font-weight:700;font-size:26px;color:#2e2e2e}
.card-web{position:absolute;left:12px;bottom:10px;font-size:8px;color:var(--muted)}
</style>
</head>
<body>

<section class="sheet flyer-front">
  <div class="sparkle" role="img" aria-label="Decorative sparkle light"></div>
  <div class="brand" style="left:0;right:0;top:18px">
    <div class="brand-dot"></div>
    <div class="brand-name">ReelVows</div>
  </div>
  <h1 class="headline" style="top:108px">Videography <span class="accent">+</span> Photography<br>packages starting at <span class="accent">$1,995</span></h1>
  <div class="photo" role="img" aria-label="Wedding photo of a bride and groom"></div>
  <div class="serves">
    <h3>Serves</h3>
    <p>Toronto | Montreal | Ottawa | Vancouver | Calgary | Edmonton</p>
  </div>
  <div class="contact-row">
    <div>Ph: 1.877.555.0148<br>Cell: 1.877.555.0148</div>
    <div class="right">www.reelvows-example.ca<br>reelvows-example.ca/social</div>
  </div>
  <footer class="footer-bar"><span>Call us: <b>1.877.555.0148</b></span><span>email: info@reelvows-example.ca</span></footer>
</section>

<section class="sheet flyer-back">
  <div class="brand" style="left:150px;top:18px">
    <div class="brand-dot"></div>
    <div class="brand-name">ReelVows</div>
  </div>
  <ul class="city-menu">
    <li>Services</li><li>Toronto</li><li>Montreal</li><li>Ottawa</li><li>Vancouver</li><li>Calgary</li><li>Edmonton</li>
  </ul>
  <h2 class="headline" style="top:108px;font-size:20px">Videography + Photography<br>packages starting at $1,995</h2>
  <div class="packages">
    <h4>WEDDING VIDEOGRAPHY PACKAGES</h4>
    <p class="lead">All our wedding videography packages include:</p>
    <ul>
      <li>Video recorded in 1080p HD using modern cameras</li>
      <li>Editing by a trained and experienced team</li>
      <li>Guests and ceremony audio with clear sound</li>
      <li>Locations: Bridal Prep, Ceremony, Group Photos</li>
      <li>Ceremony, First Dance and Reception highlights</li>
      <li>Wedding story highlights and full-length feature</li>
      <li>Delivered in standard style packaging</li>
      <li>Raw footage on request on DVD or Blu-ray</li>
    </ul>
    <h4>WEDDING PHOTOGRAPHY PACKAGES</h4>
    <p class="lead">All our wedding photography packages include:</p>
    <ul>
      <li>Unlimited number of photos</li>
      <li>Unlimited locations within the allotted timeframe</li>
      <li>All photos are provided in maximum resolution on DVD</li>
      <li>A custom online photo gallery with your best shots</li>
      <li>Color correction and retouch of every image</li>
      <li>Prints and enlargements at preferred lab pricing</li>
    </ul>
  </div>
  <p class="offer">Book Videography and Photography<br>together and get 10% off</p>
  <div class="contact-row" style="top:520px"><div>www.reelvows-example.ca</div><div class="right">reelvows-example.ca/social</div></div>
  <footer class="footer-bar"><span>Call us: <b>1.877.555.0148</b></span><span>email: info@reelvows-example.ca</span></footer>
</section>

<section class="card card-front">
  <p class="card-cities">Toronto, Montreal, Ottawa, Vancouver, Calgary, Edmonton</p>
  <div class="brand card-brand">
    <div class="brand-dot"></div>
    <div class="brand-name">ReelVows</div>
  </div>
  <div class="card-contact">
    P: 1.877.555.0148<br>E: info@reelvows-example.ca<br>www.reelvows-example.ca<br>reelvows-example.ca/social
  </div>
</section>

<section class="card card-back">
  <div class="card-mark">ReelVows</div>
  <p class="card-web">www.reelvows-example.ca</p>
</section>

</body>
</html>
```